Advertisement Design Project

Attached is the information I need in a big color ad

10X11 that will go in a weekly local paper.
I am open to color and graphics-no pictures of people please.

My logo is also attached, which I would like in the ad.

Sorry for the short notice-I just got a deal on the space and it is due Friday.

```html
<!DOCTYPE html>
<html lang="en">
<head>
<meta charset="utf-8">
<title>Estate Planning Workshop</title>
<link rel="stylesheet" href="https://fonts.googleapis.com/css2?family=Ubuntu:wght@400;500&display=swap">
<style>
  :root {
    --cream: #fcf4e4;
    --cream-light: #fffaf0;
    --peach: #f6d9a4;
    --amber: #f2b84a;
    --ink: #231f1c;
  }
  html, body {
    margin: 0;
    padding: 0;
    overflow: hidden;
  }
  .ad {
    position: relative;
    width: 1091px;
    height: 1200px;
    overflow: hidden;
    background: var(--cream);
    font-family: "Ubuntu", sans-serif;
    color: var(--ink);
  }
  .ad__backdrop {
    position: absolute;
    inset: 0;
    background:
      radial-gradient(ellipse 30% 70% at 8% 40%, var(--peach) 0%, transparent 70%),
      radial-gradient(ellipse 22% 60% at 78% 65%, rgba(242,184,74,0.35) 0%, transparent 70%),
      radial-gradient(ellipse 40% 30% at 55% 20%, var(--cream-light) 0%, transparent 80%),
      linear-gradient(160deg, var(--cream-light) 0%, var(--cream) 50%, #f9e7c4 100%);
  }
  .brand {
    position: absolute;
    top: 34px;
    right: 44px;
    width: 170px;
    text-align: center;
  }
  .brand__dot {
    display: block;
    width: 44px;
    height: 44px;
    margin: 0 auto 12px;
    border-radius: 50%;
    background: var(--amber);
  }
  .brand__name {
    font-size: 24px;
    font-weight: 500;
    color: var(--amber);
  }
  .line {
    position: absolute;
    margin: 0;
    white-space: nowrap;
  }
  .headline {
    left: 41px;
    font-size: 35px;
    font-weight: 400;
    line-height: 1;
  }
  .topic {
    font-size: 20.5px;
    line-height: 1;
  }
  .details {
    left: 92px;
    font-size: 20.5px;
    line-height: 1;
  }
</style>
</head>
<body>
<main class="ad">
  <div class="ad__backdrop" role="img" aria-label="Soft cream and amber sweeping light streaks"></div>

  <div class="brand">
    <span class="brand__dot"></span>
    <span class="brand__name">Hartwell Law</span>
  </div>

  <h1 class="line headline" style="top:34px">New Tax Laws</h1>
  <h1 class="line headline" style="top:118px">Trusts</h1>
  <h1 class="line headline" style="top:206px">Annuities and Long Term Care</h1>

  <p class="line topic" style="left:202px;top:253px">*Come learn what you need to know</p>

  <p class="line topic" style="left:167px;top:293px">* Is a living trust right for me?</p>
  <p class="line topic" style="left:167px;top:317px">* Does my existing Trust need to be changed?</p>
  <p class="line topic" style="left:167px;top:341px">* Why does Joint Tenancy create tax problems?</p>
  <p class="line topic" style="left:185px;top:364px">* I have a will, isn’t that enough?</p>
  <p class="line topic" style="left:202px;top:389px">* Why do I need powers of attorney?</p>
  <p class="line topic" style="left:202px;top:413px">*How much are inheritance taxes?</p>
  <p class="line topic" style="left:202px;top:437px">*What are the new Affordable Care Act taxes?</p>
  <p class="line topic" style="left:202px;top:461px">*How does Long Term Care insurance work?</p>
  <p class="line topic" style="left:202px;top:485px">* The average cost of long term care is over 80K a year-</p>
  <p class="line topic" style="left:202px;top:509px">how do I plan for those costs?</p>
  <p class="line topic" style="left:202px;top:560px">* The truth about annuites-</p>
  <p class="line topic" style="left:202px;top:585px">*What are the biggest mistakes in estate planning?</p>

  <p class="line details" style="top:609px">Presented by:</p>
  <p class="line details" style="top:633px">maren ellis hartwell</p>
  <p class="line details" style="top:657px">Attorney at Law</p>
  <p class="line details" style="top:682px">418 Alder Lane, Brookvale.</p>
  <p class="line details" style="top:707px">Helping&nbsp; Families plan their estates for over 20 years.</p>

  <p class="line details" style="top:756px">Trust****relationship***integrity</p>

  <p class="line details" style="top:806px">Workshop Times:</p>
  <p class="line details" style="top:855px">September 19, 2013</p>
  <p class="line details" style="top:905px">1-2:30pm</p>
  <p class="line details" style="top:956px">6-7:30pm</p>

  <p class="line details" style="top:1003px">Harborview Inn, Linwood</p>
  <p class="line details" style="top:1028px">1250 Cedar Ridge Court</p>
  <p class="line details" style="top:1053px">Linwood, California 95999</p>

  <p class="line details" style="top:1104px">Seating is limited for a Reservation please call:</p>
  <p class="line details" style="top:1154px">(555)&nbsp; 014-2290</p>
</main>
</body>
</html>
```